Zielgruppe
Weinkellerei aus Baden (Deutschland) mit Fokus im Lebensmittelhandel in Deutschland
Aufgabenstellung
Wir suchen ein Frontetikett für einen modernen badischen Rotwein (Cuvée Noir) mit dem Namen 'The quiet hour of Velmar'
Aus dem Etikett soll hervorgehen, dass es sich nicht um einen klassischen, leichten deutschen Rotwein handelt, sondern um einen kräftigen, gehaltvollen, mediterran anmutenden Rotwein mit purpurroter Farbe und vollmundigem, nachhaltigem Geschmack. (Geschmacksrichtung feinherb)
Zielgruppe Discount-Kunden, Männlich/Weiblich, Alter: 25-60 Jahre, wird für unter € 5,-/Fl. verkauft.
Weinbeschreibung:
Farbe: Ein wunderschönes tiefdunkles purpurrot mit violetten Reflexen
Duft: In der Nase zeigen sich Aromen nach Waldbeeren, sowie Anklänge von Rauch, Röstaromen, Nelke, etwas Vanille und dunkle Schokolade
Geschmack: Geschmacklich füllig und kraftvoll, Brombeeraromen und schön eingebundenen Tanninen. Langanhaltend intensiv im Abgang.
Anforderungen Etikett:
Maße: Höhe max. 120mm/Breite max. 80mm (darf auch kleiner oder quadratisch sein)
SK Etikett, Naturstruktur bis 90g (m²) (Ein - oder zweiteilig)
Eine figürliche Etikettenkontur ist möglich, es wird aber am rechten Etikettenrand eine gerade Spendekante benötigt um das Etikett maschinell verarbeiten zu können.
Als Flasche wird eine 0,75 L Bordeauxflasche (Farbe: grün) eingesetzt.
Verschluss: Longcap
Mögliche Veredelungen: Quelllack, Prägungen, Heissfolie, Glanzlack
Pflichtangaben:
The quiet hour of Velmar

```html
<!DOCTYPE html>
<html lang="de">
<head>
<meta charset="utf-8">
<title>The quiet hour of Velmar – Frontetikett</title>
<link rel="stylesheet" href="https://fonts.googleapis.com/css2?family=Josefin+Sans:wght@600&family=Allura&display=swap">
<style>
  :root {
    --page: #ffffff;
    --label-bg: #020202;
    --moon-light: rgba(192, 191, 193, 0.55);
    --shade-slate: rgba(75, 85, 80, 0.7);
    --shade-wine: rgba(168, 32, 42, 0.7);
    --title: #c9c8ca;
    --script-slate: #5a5a5a;
    --script-wine: #a8202a;
  }
  html, body {
    margin: 0;
    padding: 0;
    width: 1200px;
    height: 896px;
    overflow: hidden;
    background: var(--page);
  }
  .sheet {
    width: 1200px;
    height: 896px;
    display: flex;
    justify-content: center;
    align-items: center;
    gap: 80px;
  }
  .label {
    position: relative;
    width: 380px;
    height: 522px;
    background: var(--label-bg);
    overflow: hidden;
  }
  .label--slate { --shade: var(--shade-slate); --script: var(--script-slate); }
  .label--wine  { --shade: var(--shade-wine);  --script: var(--script-wine); }
  .night-sky {
    position: absolute;
    left: 20px;
    top: 17px;
    width: 340px;
    height: 340px;
    background:
      radial-gradient(circle at 50% 50%,
        rgba(0,0,0,0) 0%,
        rgba(0,0,0,0) 50%,
        var(--moon-light) 66%,
        var(--shade) 76%,
        rgba(0,0,0,0) 90%),
      radial-gradient(ellipse at 50% 50%,
        rgba(200,199,201,0.18) 0%,
        rgba(0,0,0,0) 45%);
  }
  .wine-name {
    position: absolute;
    left: 0;
    right: 0;
    top: 372px;
    margin: 0;
    text-align: center;
    font-weight: normal;
  }
  .wine-name__main {
    display: block;
    font-family: "Josefin Sans", sans-serif;
    font-weight: 600;
    font-size: 39px;
    letter-spacing: 1px;
    color: var(--title);
    line-height: 1;
  }
  .wine-name__script {
    display: block;
    margin-top: -6px;
    font-family: "Allura", cursive;
    font-size: 74px;
    line-height: 1;
    color: var(--script);
  }
</style>
</head>
<body>
<main class="sheet">
  <article class="label label--slate">
    <div class="night-sky" role="img" aria-label="Ring of moon phases in grey around a scattered star field"></div>
    <h1 class="wine-name">
      <span class="wine-name__main">THE QUIET HOUR</span>
      <span class="wine-name__script">of Velmar</span>
    </h1>
  </article>

  <article class="label label--wine">
    <div class="night-sky" role="img" aria-label="Ring of moon phases in grey and wine red around a scattered star field"></div>
    <h2 class="wine-name">
      <span class="wine-name__main">THE QUIET HOUR</span>
      <span class="wine-name__script">of Velmar</span>
    </h2>
  </article>
</main>
</body>
</html>
```